Health Coaching Flyer for New Clients

I need a two-sided flyer (3.5" x 8.5" preferred or 5" x 7") to distribute to potential coaching clients. My business name is Talvora Health & Wellness Coaching. My business is focused on helping people with habit changes that contribute to their overall well-being. I would like the design colors to be gender neutral. I would like a small photo of myself near the "my name is Jen" statement. Please feel free to change the logo color to match the design.

Target Market(s)

Adults of all ages.

Font styles to use
Serif

Requirements
Must have
• Emphasize my opening question (found in health coaching brochure - attached).
• Small picture of myself near "my name is Jen" statement.
Should not have
• No light of pastel colors.

```html
<!DOCTYPE html>
<html lang="en">
<head>
<meta charset="utf-8">
<title>Talvora Health &amp; Wellness Coaching – Flyer</title>
<link href="https://fonts.googleapis.com/css2?family=Roboto+Slab:wght@400;700;800&display=swap" rel="stylesheet">
<style>
  :root{
    --sky:#87cdf2;
    --navy:#154c8f;
    --coral:#ee5a5a;
    --ink:#1f2a44;
    --paper:#ffffff;
    --backdrop:#5a5a5c;
  }
  *{box-sizing:border-box;margin:0;padding:0}
  html,body{width:1200px;height:849px;overflow:hidden}
  body{background:var(--backdrop);position:relative;font-family:"Roboto Slab",Georgia,serif;color:var(--ink)}
  .page{position:absolute;top:69px;width:511px;height:716px;background:var(--paper);overflow:hidden}
  .page--front{left:69px}
  .page--back{left:610px}

  /* front */
  .front-hero{position:absolute;left:0;top:0;width:100%;height:446px;background:var(--sky)}
  .headline{position:absolute;left:0;top:30px;width:100%;text-align:center;color:var(--paper);font-weight:800;font-size:52px;letter-spacing:.5px;line-height:1}
  .headline small{font-size:24px;font-weight:400}
  .subhead{position:absolute;left:0;top:86px;width:100%;text-align:center;color:var(--navy);font-size:25px;line-height:32px;font-weight:400}
  .subhead .light{color:var(--paper)}
  .hero-art{position:absolute;left:69px;top:182px;width:390px;height:278px;background:linear-gradient(90deg,#ee5a5a 0%,#f3a3a3 28%,#bfe6fa 50%,#1d5a9e 72%,#ee5a5a 100%);border-radius:120px 120px 0 0}
  .portrait{position:absolute;left:31px;top:489px;width:87px;height:113px;background:linear-gradient(160deg,#6b4b3e,#d9a58a 60%,#8d6a5a)}
  .bio{position:absolute;left:132px;top:487px;width:352px;font-size:12.4px;line-height:17.2px}

  .brand{position:absolute;left:0;width:100%;display:flex;justify-content:center;align-items:center;gap:10px;color:var(--navy);font-weight:700}
  .brand__text{text-align:left;line-height:1}
  .brand__name{display:block;font-size:36px;letter-spacing:4px}
  .brand__sub{display:block;font-size:11.5px;letter-spacing:.3px;margin-top:4px}
  .brand__mark{width:22px;height:22px;background:var(--coral)}
  .page--front .brand{top:637px}
  .page--back .brand{top:26px}

  /* back */
  .back-band{position:absolute;left:0;top:95px;width:100%;height:483px;background:var(--sky)}
  .back-title{position:absolute;left:30px;top:117px;color:var(--navy);font-weight:800;font-size:26.5px;letter-spacing:.2px}
  .benefits{position:absolute;left:29px;top:168px;width:165px;list-style:none;font-size:12.4px;line-height:17.2px}
  .benefits li{position:relative;padding-left:10px;margin-bottom:5px}
  .benefits li::before{content:"";position:absolute;left:0;top:3px;width:3px;height:9px;background:var(--coral)}
  .coach-art{position:absolute;left:199px;top:164px;width:275px;height:245px;background:radial-gradient(circle at 55% 50%,#154c8f 0 38%,#ee5a5a 39% 55%,#8dd1f3 56%);border-radius:10px}
  .divider{position:absolute;left:206px;top:425px;width:1px;height:132px;background:var(--navy)}
  .invite{position:absolute;left:222px;top:424px;width:270px;font-size:12.3px;line-height:17.2px;font-style:italic;font-weight:700;color:var(--navy)}
  .invite p+p{margin-top:17px}
  .contact{position:absolute;left:0;top:592px;width:100%;text-align:center}
  .contact__lead{font-size:18.5px}
  .contact__note{font-size:12.4px;margin-top:2px}
  .contact__name{font-size:24px;font-weight:800;color:var(--coral);margin-top:18px;line-height:1}
  .contact__line{display:flex;justify-content:center;align-items:center;gap:6px;font-size:17.5px;margin-top:6px}
  .contact__line svg{width:15px;height:15px}
  .contact__line .gap{width:4px}
</style>
</head>
<body>
  <section class="page page--front">
    <div class="front-hero"></div>
    <h1 class="headline">NEED SUPPORT <small>in</small></h1>
    <p class="subhead">MAKING REAL, LASTING LIFESTYLE<br><span class="light">and</span> BEHAVIOR CHANGES?</p>
    <div class="hero-art" role="img" aria-label="Illustration of two facing profile heads joined by a bridge, with a businessman running across between them"></div>
    <div class="portrait" role="img" aria-label="Portrait photo of Jen, the coach"></div>
    <p class="bio">My name is Jen.&nbsp; I am studying to become an KESTREL-Certified Functional Health Coach.&nbsp; My training involves many science-based practices that improve both our health and how we grow and change as humans.&nbsp; I now have the opportunity to turn that knowledge into practice by coaching actual clients interested in improving their own health and well-being.</p>
    <div class="brand">
      <span class="brand__text"><span class="brand__name">TALVORA</span><span class="brand__sub">HEALTH &amp; WELLNESS COACHING</span></span>
      <span class="brand__mark"></span>
    </div>
  </section>

  <section class="page page--back">
    <div class="brand">
      <span class="brand__text"><span class="brand__name">TALVORA</span><span class="brand__sub">HEALTH &amp; WELLNESS COACHING</span></span>
      <span class="brand__mark"></span>
    </div>
    <div class="back-band"></div>
    <h2 class="back-title">FUNCTIONAL HEALTH COACHES...</h2>
    <ul class="benefits">
      <li>Leverage your strengths rather than focus on your weaknesses</li>
      <li>Support you in finding your own strategies and motivation for change</li>
      <li>Provide a judgment-free zone and support your autonomy</li>
      <li>Use an experimental mindset to find and develop sustainable habits</li>
      <li>Act as your accountability partner as you reach your unique health goals; whether they be improving sleep, diet, fitness, social connection, or reducing stress.</li>
    </ul>
    <div class="coach-art" role="img" aria-label="Illustration of a head silhouette with a medical cross, surrounded by health icons, leaves and a clipboard"></div>
    <div class="divider"></div>
    <div class="invite">
      <p>I would like to invite you to participate with me as a client as I continue to hone my coaching skills. We can develop a plan and schedule that aligns with your goals.</p>
      <p>As a way to give back to my community, I am offering new clients six free coaching sessions.&nbsp; This is a limited time offer.</p>
    </div>
    <div class="contact">
      <p class="contact__lead">Please contact me.</p>
      <p class="contact__note">I’m ready to support you as you work to improve your health.</p>
      <p class="contact__name">JEN TALVORA</p>
      <p class="contact__line">
        <svg viewBox="0 0 16 16" aria-hidden="true"><rect width="16" height="16" rx="2" fill="#ee5a5a"/><path d="M5 3.5l2 2-1 1.3c.6 1.4 1.7 2.5 3.2 3.2l1.3-1 2 2-1.2 1.5C7.8 12.3 3.7 8.2 3.5 4.7z" fill="#fff"/></svg>
        <span>555-014-2870</span><span class="gap"></span>
        <svg viewBox="0 0 16 16" aria-hidden="true"><rect x="1" y="3.5" width="14" height="10" fill="#ee5a5a"/><path d="M1 3.5l7 5.5 7-5.5" fill="none" stroke="#fff" stroke-width="1.3"/></svg>
        <span>hello@talvoracoaching.example</span>
      </p>
    </div>
  </section>
</body>
</html>
```